We sell companies excess stock for them

We need a business card for a company based in New Zealand called 'ShelfLark'.

Check out our website to get an idea www.shelflark.example

We help other businesses to;
- Sell Excess Stock
- Manage Product Returns
- Sell Company Assets

Our logo is attached for your reference
The font used is 'RifficFree-Bold'

Target Market(s)

Businesses

Industry/Entity Type

Business

Contact Information for Business Card

Name: Mara Quillby
Phone: 027 864 3190
email: maraquillby@shelflark.example
website: www.shelflark.example

Font styles to use
Other font styles liked:

Colors
9bcb3b

Requirements
Must have
Nice to have
Should not have

```html
<!DOCTYPE html>
<html lang="en">
<head>
<meta charset="utf-8">
<title>ShelfLark business card</title>
<link rel="stylesheet" href="https://fonts.googleapis.com/css2?family=Fredoka:wght@700&family=Open+Sans:wght@400;600&display=swap">
<style>
  :root {
    --stage: #2e2a28;
    --card-white: #ffffff;
    --brand-green: #9bcb3b;
    --brand-green-deep: #86b52c;
    --ink: #2a2a2a;
    --ink-soft: #3c3c3c;
    --rule: #c9c9c9;
    --mascot-orange: #f2a33a;
  }
  * { box-sizing: border-box; margin: 0; padding: 0; }
  html, body {
    width: 1200px; height: 844px; overflow: hidden;
    background: var(--stage);
  }
  .stage {
    position: relative; width: 1200px; height: 844px;
    display: flex; align-items: center; justify-content: center; gap: 60px;
  }
  .card {
    position: relative; width: 520px; height: 300px;
    box-shadow: 0 10px 30px rgba(0,0,0,0.45);
  }
  .card-front { background: var(--card-white); }
  .card-back { background: var(--brand-green); }

  .mascot {
    position: absolute;
    border-radius: 14px;
    background: linear-gradient(135deg, var(--brand-green) 0%, var(--mascot-orange) 70%);
  }
  .card-front .mascot { left: 232px; top: 22px; width: 96px; height: 68px; }
  .card-back .mascot { left: 170px; top: 60px; width: 190px; height: 150px; opacity: .95; }

  .rule { position: absolute; left: 70px; right: 70px; height: 1px; background: var(--rule); }
  .rule-top { top: 100px; }
  .rule-bottom { top: 272px; }

  .wordmark {
    position: absolute; left: 0; right: 0; top: 104px;
    text-align: center;
    font-family: "Fredoka", sans-serif; font-weight: 700;
    font-size: 58px; line-height: 1; letter-spacing: -1px;
    color: var(--ink);
  }
  .contact {
    position: absolute; left: 0; right: 0; top: 176px;
    display: flex; flex-direction: column; align-items: center;
    font-family: "Open Sans", sans-serif; color: var(--ink-soft);
  }
  .contact-name { font-weight: 600; font-size: 21px; color: var(--ink); margin-bottom: 4px; }
  .contact-name .surname { color: var(--brand-green); }
  .contact-list { list-style: none; font-size: 13.5px; line-height: 20px; }
  .contact-list li { display: flex; align-items: center; gap: 7px; }
  .contact-list svg { width: 11px; height: 11px; fill: var(--ink-soft); flex: none; }
</style>
</head>
<body>
<main class="stage">
  <section class="card card-front" aria-label="Card front">
    <div class="mascot" role="img" aria-label="Mascot illustration: delivery runner in green cap carrying an orange parcel"></div>
    <div class="rule rule-top"></div>
    <div class="wordmark">ShelfLark</div>
    <div class="contact">
      <p class="contact-name">Mara <span class="surname">Quillby</span></p>
      <ul class="contact-list">
        <li><svg viewBox="0 0 24 24" aria-hidden="true"><path d="M6.6 10.8a15 15 0 0 0 6.6 6.6l2.2-2.2a1 1 0 0 1 1-.25 11.4 11.4 0 0 0 3.6.6 1 1 0 0 1 1 1V20a1 1 0 0 1-1 1A17 17 0 0 1 3 4a1 1 0 0 1 1-1h3.5a1 1 0 0 1 1 1c0 1.25.2 2.45.6 3.6a1 1 0 0 1-.25 1z"/></svg>027 864 3190</li>
        <li><svg viewBox="0 0 24 24" aria-hidden="true"><path d="M2 5h20v14H2z M4 7v1l8 5 8-5V7l-8 5z" fill-rule="evenodd"/></svg>maraquillby@shelflark.example</li>
        <li><svg viewBox="0 0 24 24" aria-hidden="true"><circle cx="12" cy="12" r="10"/></svg>www.shelflark.example</li>
      </ul>
    </div>
    <div class="rule rule-bottom"></div>
  </section>

  <section class="card card-back" aria-label="Card back">
    <div class="mascot" role="img" aria-label="Large mascot illustration: delivery runner giving a thumbs up with an orange parcel"></div>
  </section>
</main>
</body>
</html>
```